Personal Trainer needs a catchy not cheesy flyer to advertise.

CONTENT:

'personal training introductory offer 4x1 hour sessions for $199'

Check list with 'tick' next to them
-Are you unsure of how to successfully program workouts?
-Would you like to loose fat and or build muscle?
-Want to feel healthier and fitter
-Want better posture
-Would you like more energy during the day?

PLEASE Email Brett Marlowe @ brett@tallowpeak.com.au with the 'subject' "PT Special" and we will get back to you!

The colours blue and green would be best to use.
No pictures of half naked people training.
male and female in mid 30's having fun and exercising 1-2 pictures ( or it could just have pictures of exercise equipment kettle bells, dumbells, barbells, no machines)

Terms and conditions apply in small print

Industry/Entity Type

Personal Trainer

Requirements
Must have
• TICKS next to each check list.
• 'Krest Gym 24/7' logo at bottom of page I could not up load picture can just get from internet.

```html
<!DOCTYPE html>
<html lang="en">
<head>
<meta charset="utf-8">
<title>Personal Training – Introductory Offer</title>
<link href="https://fonts.googleapis.com/css2?family=Anton&family=Cinzel:wght@400&family=Roboto+Condensed:wght@400;700&display=swap" rel="stylesheet">
<style>
  :root {
    --band-blue: #1d3f94;
    --band-blue-dark: #122a6b;
    --band-edge: #3f6fd0;
    --navy: #1a2a6c;
    --white: #ffffff;
    --orange: #f07d16;
    --amber: #f7a524;
    --yellow: #fbe57a;
    --cream: #fff6d6;
    --ink: #1b1b1b;
    --brand-red: #c8181e;
  }
  html, body { margin: 0; padding: 0; overflow: hidden; }
  body { width: 1200px; height: 2541px; }
  .flyer {
    position: relative;
    width: 1200px; height: 2541px; overflow: hidden;
    background: radial-gradient(ellipse 1000px 1500px at 850px 1280px, var(--cream) 0%, var(--yellow) 35%, var(--amber) 72%, var(--orange) 100%);
    font-family: "Roboto Condensed", "Arial Narrow", sans-serif;
  }
  .side-band {
    position: absolute; left: 0; top: 0; width: 252px; height: 100%;
    background: linear-gradient(90deg, var(--band-edge) 0, var(--band-edge) 34px, var(--band-blue-dark) 42px, var(--band-blue) 140px, var(--band-blue-dark) 246px);
  }
  .side-band::before, .side-band::after {
    content: ""; position: absolute; top: 0; bottom: 0; width: 7px; background: var(--white);
  }
  .side-band::before { left: 36px; }
  .side-band::after { right: 0; }
  .side-title {
    position: absolute; left: 58px; top: 230px; height: 2180px; width: 180px;
    writing-mode: vertical-rl; transform: rotate(180deg);
    font-family: "Cinzel", Georgia, serif; font-weight: 400;
    font-size: 150px; letter-spacing: 16px; color: var(--white);
    text-align: center; line-height: 180px; white-space: nowrap;
  }
  .offer-header { position: absolute; left: 0; top: 0; }
  .offer-kicker, .offer-line { font-family: "Roboto Condensed", "Arial Narrow", sans-serif; font-weight: 700; fill: var(--navy); }
  .price, .price-for { font-family: "Anton", Impact, sans-serif; fill: var(--white); }
  .checklist {
    position: absolute; left: 440px; top: 700px; width: 700px; margin: 0; padding: 0; list-style: none;
  }
  .checklist li {
    position: relative; padding-left: 72px; margin-bottom: 38px;
    font-size: 40px; font-weight: 700; line-height: 48px; color: var(--ink);
  }
  .checklist .tick { position: absolute; left: 0; top: 2px; width: 54px; height: 48px; }
  .contact {
    position: absolute; left: 430px; width: 770px; top: 1350px; text-align: center;
    font-size: 30px; line-height: 40px; color: var(--ink);
  }
  .contact strong { display: block; }
  .photo {
    position: absolute; left: 300px; top: 1560px; width: 900px; height: 840px;
    background: linear-gradient(100deg, rgba(200,140,95,0.55) 0%, rgba(176,118,80,0.6) 45%, rgba(90,90,90,0.55) 75%, rgba(60,60,60,0.6) 100%);
  }
  .brand {
    position: absolute; right: 48px; top: 2230px; display: flex; align-items: center; gap: 14px;
    font-family: "Roboto Condensed", "Arial Narrow", sans-serif; font-weight: 700;
    font-size: 54px; color: var(--brand-red); white-space: nowrap;
  }
  .brand-dot { width: 28px; height: 28px; border-radius: 50%; background: var(--brand-red); }
  .terms {
    position: absolute; left: 430px; top: 2418px; font-size: 26px; color: var(--ink);
  }
</style>
</head>
<body>
<main class="flyer">
  <div class="side-band"><div class="side-title">Personal Training</div></div>

  <svg class="offer-header" width="1200" height="650" viewBox="0 0 1200 650">
    <text class="offer-kicker" x="683" y="92" font-size="50" text-anchor="middle" textLength="300" lengthAdjust="spacingAndGlyphs">OFFERING</text>
    <text class="offer-line" x="427" y="192" font-size="104" textLength="683" lengthAdjust="spacingAndGlyphs">4X1 HOUR SESSIONS</text>
    <text class="price-for" transform="translate(530 512) rotate(-90)" x="0" y="0" font-size="118" textLength="250" lengthAdjust="spacingAndGlyphs">FOR</text>
    <text class="price" x="540" y="612" font-size="470" textLength="590" lengthAdjust="spacingAndGlyphs">$199</text>
  </svg>

  <ul class="checklist">
    <li><svg class="tick" viewBox="0 0 56 50"><path d="M5 28 L20 43 L51 7" fill="none" stroke="#1a2a6c" stroke-width="9" stroke-linecap="round" stroke-linejoin="round"/></svg>Are you unsure of how to successfully program workouts?</li>
    <li><svg class="tick" viewBox="0 0 56 50"><path d="M5 28 L20 43 L51 7" fill="none" stroke="#1a2a6c" stroke-width="9" stroke-linecap="round" stroke-linejoin="round"/></svg>Would you like to loose fat and or build muscle?</li>
    <li><svg class="tick" viewBox="0 0 56 50"><path d="M5 28 L20 43 L51 7" fill="none" stroke="#1a2a6c" stroke-width="9" stroke-linecap="round" stroke-linejoin="round"/></svg>Want to feel healthier and fitter</li>
    <li><svg class="tick" viewBox="0 0 56 50"><path d="M5 28 L20 43 L51 7" fill="none" stroke="#1a2a6c" stroke-width="9" stroke-linecap="round" stroke-linejoin="round"/></svg>Want better posture</li>
    <li><svg class="tick" viewBox="0 0 56 50"><path d="M5 28 L20 43 L51 7" fill="none" stroke="#1a2a6c" stroke-width="9" stroke-linecap="round" stroke-linejoin="round"/></svg>Would you like more energy during the day?</li>
  </ul>

  <div class="contact">
    <strong>PLEASE</strong>
    Email Brett Marlowe at<br>
    brett@tallowpeak.com.au<br>
    with the 'subject' "PT Special" and we will get back to you!
  </div>

  <div class="photo" role="img" aria-label="Woman in workout clothes stretching on the floor beside a set of dumbbells and weight plates"></div>

  <div class="brand"><span class="brand-dot"></span>Krest Gym 24/7</div>

  <div class="terms">Terms and conditions apply</div>
</main>
</body>
</html>
```